business card and flyer/pricelist

Business Name: Fern Locks Westbrook
new boutique salon run from home, using Australian owned natural products and colours, we need a flyer design to do a letter box drop to advertise the business as well as incorporating a price list on the front (single sided with writing on front and only colour on back)

The salon has a natural feel with light coloured timber chairs, bamboo timber bench top and shelving.

we are after a natural toned colour for the flyer, with possibly a brown/darkish colour writing

we are after a flyer that will also be able to use the design heading (business name) for business cards as well

feel free to look on my pintrest account to get a feel for my style under Marla Quenby.

I love simple clean and Natural looks.

Font styles to use
Script
Other font styles liked:
• SCRIPT HANDWRITTEN FONTS

Colors
cadf82
e9f1ce
5c5c5c
d3d3d3
add136
fee18a

Requirements
Must have
• NATURAL COLOURINGS, eg soft greens, browns,
white or off white background.
Should not have
• photos,

```html
<!DOCTYPE html>
<html lang="en">
<head>
<meta charset="utf-8">
<title>Fern Locks Westbrook – Flyer &amp; Price List</title>
<link rel="stylesheet" href="https://fonts.googleapis.com/css2?family=Parisienne&family=Great+Vibes&family=Lora:ital,wght@1,500;1,600&family=Open+Sans:wght@600;700;800&display=swap">
<style>
  :root {
    --lime: #afd13a;
    --cream: #eef3d6;
    --brown: #5a1f0f;
    --white: #ffffff;
    --grey: #5c5c5c;
    --paper: #e6e7e8;
  }
  * { box-sizing: border-box; margin: 0; padding: 0; }
  html, body { width: 1200px; height: 1200px; overflow: hidden; }
  body { background: var(--paper); position: relative; font-family: "Lora", Georgia, serif; color: var(--brown); }

  .card { position: absolute; top: 150px; width: 420px; height: 900px; overflow: hidden; }
  .flyer-front { left: 140px; background: var(--lime); }
  .flyer-back { left: 640px; background: var(--lime); }

  /* front */
  .front-shapes { position: absolute; inset: 0; }
  .brand { position: absolute; top: 26px; left: 40px; width: 350px; }
  .brand-name { font-family: "Parisienne", cursive; font-size: 58px; line-height: 1; }
  .brand-place { font-family: "Parisienne", cursive; font-size: 22px; text-align: right; margin-top: -6px; padding-right: 40px; }

  .offer-band {
    position: absolute; left: 44px; top: 290px; width: 82px; height: 440px;
    background: var(--brown); border-radius: 10px;
    display: flex; justify-content: center; align-items: center;
  }
  .offer-text {
    writing-mode: vertical-rl; transform: rotate(180deg);
    font-family: "Open Sans", Arial, sans-serif; color: var(--white);
    display: flex; flex-direction: column; align-items: flex-start;
  }
  .offer-line { font-size: 17px; font-weight: 600; white-space: nowrap; }
  .offer-line .big { font-size: 34px; font-weight: 800; margin-top: 10px; }
  .offer-visit {
    background: var(--lime); color: var(--brown); font-size: 20px; font-weight: 700;
    padding: 10px 4px; margin-top: 2px; white-space: nowrap;
  }

  .price-list { position: absolute; left: 138px; top: 200px; width: 252px; font-size: 13px; font-style: italic; font-weight: 600; }
  .price-group { margin-bottom: 6px; }
  .price-heading { font-family: "Great Vibes", cursive; font-size: 24px; font-weight: 400; font-style: normal; line-height: 1.1; }
  .price-row { display: flex; align-items: baseline; line-height: 17px; }
  .price-item { white-space: nowrap; }
  .price-leader { flex: 1; border-bottom: 2px dotted var(--brown); margin: 0 4px; transform: translateY(-4px); opacity: .7; }
  .price-amount { white-space: nowrap; }
  .price-note { line-height: 17px; }

  .contact { position: absolute; left: 0; right: 0; top: 802px; text-align: center; font-size: 14px; font-style: italic; font-weight: 600; }
  .contact-line { display: flex; justify-content: center; align-items: center; gap: 5px; line-height: 20px; }
  .contact-icon { width: 12px; height: 12px; }
  .payments {
    position: absolute; left: 28px; right: 28px; top: 848px; height: 38px;
    background: var(--white); border-radius: 6px;
    display: flex; align-items: center; justify-content: space-around; padding: 0 8px;
    font-family: "Open Sans", Arial, sans-serif; font-size: 13px; font-weight: 700; color: var(--grey);
  }
  .payment-mark { display: flex; align-items: center; gap: 4px; }
  .payment-dot { width: 10px; height: 10px; border-radius: 50%; background: var(--grey); }
  .partner-badge { width: 26px; height: 18px; border-radius: 3px; background: var(--paper); }

  /* back */
  .back-band { position: absolute; top: 0; bottom: 0; width: 78px; background: var(--brown); }
  .back-band.left { left: 0; }
  .back-band.right { right: 0; }
  .back-brand {
    position: absolute; left: 50%; top: 50%; width: 820px;
    transform: translate(-50%, -50%) rotate(-90deg); text-align: center;
  }
  .back-brand .brand-name { font-size: 132px; }
  .back-brand .brand-place { font-size: 46px; margin-top: -18px; padding-right: 70px; }
</style>
</head>
<body>

<section class="card flyer-front">
  <svg class="front-shapes" viewBox="0 0 420 900" width="420" height="900" aria-hidden="true">
    <path d="M0,195 C150,160 330,200 420,80 L420,745 C330,790 140,760 0,820 Z" fill="var(--cream)"/>
    <path d="M0,195 C150,160 330,200 420,80" fill="none" stroke="var(--brown)" stroke-width="6"/>
    <path d="M0,820 C140,760 330,790 420,745" fill="none" stroke="var(--brown)" stroke-width="3"/>
  </svg>

  <header class="brand">
    <div class="brand-name">Fern Locks</div>
    <div class="brand-place">westbrook</div>
  </header>

  <aside class="offer-band">
    <div class="offer-text">
      <div class="offer-line">Special introductory offer - receive <span class="big">25% OFF</span></div>
      <div class="offer-visit">YOUR INITIAL VISIT</div>
    </div>
  </aside>

  <div class="price-list">
    <div class="price-group">
      <h2 class="price-heading">Cuts</h2>
      <div class="price-row"><span class="price-item">Ladies (inc. shampoo/blowdry)</span><span class="price-leader"></span><span class="price-amount">$45</span></div>
      <div class="price-row"><span class="price-item">Mens</span><span class="price-leader"></span><span class="price-amount">$20</span></div>
      <div class="price-row"><span class="price-item">13 &amp; Under From</span><span class="price-leader"></span><span class="price-amount">$45</span></div>
      <div class="price-row"><span class="price-item">5 &amp; Under</span><span class="price-leader"></span><span class="price-amount">$10</span></div>
    </div>
    <div class="price-group">
      <h2 class="price-heading">Blowdry &amp; Styling</h2>
      <div class="price-row"><span class="price-item">Short</span><span class="price-leader"></span><span class="price-amount">$25</span></div>
      <div class="price-row"><span class="price-item">Medium</span><span class="price-leader"></span><span class="price-amount">$30</span></div>
      <div class="price-row"><span class="price-item">Long</span><span class="price-leader"></span><span class="price-amount">$40</span></div>
      <div class="price-row"><span class="price-item">Straight Iron (after blowdry)</span><span class="price-leader"></span><span class="price-amount">$10</span></div>
      <div class="price-row"><span class="price-item">Upstyles</span><span class="price-leader"></span><span class="price-amount">POA</span></div>
      <div class="price-row"><span class="price-item">Onsite styling</span><span class="price-leader"></span><span class="price-amount">$55</span></div>
    </div>
    <div class="price-group">
      <h2 class="price-heading">Colours</h2>
      <div class="price-row"><span class="price-item">Regrowth</span><span class="price-leader"></span><span class="price-amount">$55</span></div>
      <div class="price-row"><span class="price-item">Short</span><span class="price-leader"></span><span class="price-amount">$60</span></div>
      <div class="price-row"><span class="price-item">Medium</span><span class="price-leader"></span><span class="price-amount">$75</span></div>
      <div class="price-row"><span class="price-item">Long</span><span class="price-leader"></span><span class="price-amount">$85</span></div>
    </div>
    <div class="price-group">
      <h2 class="price-heading">Foils</h2>
      <div class="price-row"><span class="price-item">Top Foils</span><span class="price-leader"></span><span class="price-amount">$95</span></div>
      <div class="price-row"><span class="price-item">½ head</span><span class="price-leader"></span><span class="price-amount">$110</span></div>
      <div class="price-row"><span class="price-item">¾ head</span><span class="price-leader"></span><span class="price-amount">$145</span></div>
      <div class="price-note">Full head<br>(all include toner)</div>
    </div>
    <div class="price-group">
      <h2 class="price-heading">Treatments</h2>
      <div class="price-row"><span class="price-item">At basin</span><span class="price-leader"></span><span class="price-amount">$35</span></div>
      <div class="price-row"><span class="price-item">Special Feet From</span><span class="price-leader"></span><span class="price-amount">$10</span></div>
      <div class="price-note">Eye brow/lash treatments</div>
    </div>
  </div>

  <footer class="contact">
    <div class="contact-line">
      <svg class="contact-icon" viewBox="0 0 12 12" aria-hidden="true"><path d="M6,0.5 A4,4 0 0 1 10,4.5 C10,7.5 6,11.5 6,11.5 C6,11.5 2,7.5 2,4.5 A4,4 0 0 1 6,0.5 Z" fill="var(--brown)"/><circle cx="6" cy="4.5" r="1.5" fill="var(--lime)"/></svg>
      <span>18 Wattlebird Lane Westbrook</span>
    </div>
    <div class="contact-line">
      <svg class="contact-icon" viewBox="0 0 12 12" aria-hidden="true"><circle cx="6" cy="6" r="6" fill="var(--brown)"/><path d="M4,3 L5,3 L5.6,4.6 L4.9,5.2 C5.3,6.1 5.9,6.7 6.8,7.1 L7.4,6.4 L9,7 L9,8 C9,8.6 8.5,9 8,9 C5.2,8.8 3.2,6.8 3,4 C3,3.5 3.4,3 4,3 Z" fill="var(--lime)"/></svg>
      <span>0412555087</span>
    </div>
  </footer>
  <div class="payments">
    <span class="payment-mark">Gumleaf Pro</span>
    <span class="payment-mark"><span class="payment-dot"></span>Orbit</span>
    <span class="payment-mark">Vela</span>
    <span class="payment-mark">Tapnet</span>
    <span class="partner-badge"></span>
    <span class="payment-mark">Friendbook</span>
  </div>
</section>

<section class="card flyer-back">
  <div class="back-band left"></div>
  <div class="back-band right"></div>
  <div class="back-brand">
    <div class="brand-name">Fern Locks</div>
    <div class="brand-place">westbrook</div>
  </div>
</section>

</body>
</html>
```